Boutique PEO needs a catchy snail mail and email marketing flyer

Our company provides services to our clients and co-employees throughout the entire life cycle of an employee's employment. It is very serious business to our clients' but we need a catchy message and look to attract the attention of prospective clients. I have attached some of the ideas we tried.

Target Market(s)

small to medium size companies

Font styles to use
Serif

Colors

Designer to choose colors to be used in the design.

```html
<!DOCTYPE html>
<html lang="en">
<head>
<meta charset="utf-8">
<title>HR Headaches Flyer</title>
<link rel="stylesheet" href="https://fonts.googleapis.com/css2?family=Roboto+Condensed:wght@400;700&family=Roboto:wght@400;700&display=swap">
<style>
  :root {
    --paper: #e3e0d6;
    --band-deep: #123a6b;
    --band-mid: #1f5896;
    --band-light: #3d79b8;
    --sky: #5aaee6;
    --sky-light: #7cc3f0;
    --navy: #0c2340;
    --panel: #050709;
    --ink: #0a0a0a;
    --white: #ffffff;
    --gold-top: #ffe23a;
    --gold-bottom: #f39a12;
    --pink: #e23a9c;
    --pink-light: #f06cbd;
    --brand-blue: #1b5f9c;
    --coat-dark: #2e2b29;
    --coat-light: #ece9e3;
  }
  * { margin: 0; padding: 0; box-sizing: border-box; }
  html, body { width: 1200px; height: 825px; overflow: hidden; background: var(--paper); }
  .flyer { position: relative; width: 1200px; height: 825px; background: var(--paper); overflow: hidden; font-family: "Roboto", Arial, sans-serif; }
  .shapes { position: absolute; inset: 0; }
  .headline-small {
    position: absolute; left: 298px; top: 84px; z-index: 2;
    font-family: "Roboto Condensed", Arial, sans-serif; font-weight: 700;
    font-size: 68px; line-height: 1; color: var(--ink);
  }
  .headline-big {
    position: absolute; left: 50px; top: 156px; z-index: 2;
    font-family: "Roboto Condensed", Arial, sans-serif; font-weight: 700;
    font-size: 100px; line-height: 1; letter-spacing: 1px;
    background: linear-gradient(180deg, var(--gold-top) 0%, var(--gold-bottom) 100%);
    -webkit-background-clip: text; background-clip: text; color: transparent;
  }
  .tagline {
    position: absolute; left: 300px; top: 258px; width: 340px; z-index: 2;
    font-size: 36px; line-height: 1.12; color: var(--white); font-weight: 400;
  }
  .dog-photo {
    position: absolute; left: 36px; top: 262px; width: 320px; height: 540px; z-index: 1;
    clip-path: polygon(30px 0, 220px 0, 240px 120px, 250px 160px, 320px 300px, 320px 540px, 0 540px, 0 90px);
    background: linear-gradient(180deg, var(--coat-dark) 0%, #4a4643 45%, #cfcbc4 75%, var(--coat-light) 100%);
  }
  .brand {
    position: absolute; left: 360px; top: 650px;
    display: flex; align-items: center; gap: 10px;
    font-family: "Roboto Condensed", Arial, sans-serif; font-weight: 700;
    font-size: 26px; color: var(--brand-blue);
  }
  .brand-dot { width: 16px; height: 16px; border-radius: 50%; background: var(--pink); }
  .section-title {
    position: absolute; left: 656px; top: 79px; width: 197px; height: 568px;
    display: flex; align-items: center; justify-content: center;
  }
  .section-title span {
    transform: rotate(-90deg); white-space: nowrap;
    font-family: "Roboto Condensed", Arial, sans-serif; font-weight: 700;
    font-size: 56px; letter-spacing: 1px; color: var(--navy);
  }
  .service-copy {
    position: absolute; left: 890px; top: 268px; width: 290px;
    font-size: 24px; line-height: 1.36; color: var(--white); text-align: justify;
    hyphens: auto;
  }
  .cta {
    position: absolute; left: 760px; top: 742px; width: 420px; height: 64px;
    display: flex; align-items: center; justify-content: center;
    font-family: "Roboto Condensed", Arial, sans-serif; font-weight: 700;
    font-size: 40px; color: var(--white); letter-spacing: 0.5px;
  }
</style>
</head>
<body>
<main class="flyer">
  <svg class="shapes" width="1200" height="825" viewBox="0 0 1200 825" aria-hidden="true">
    <defs>
      <linearGradient id="band" x1="0" y1="0" x2="1" y2="1">
        <stop offset="0" stop-color="#3d79b8"/>
        <stop offset="0.5" stop-color="#1f5896"/>
        <stop offset="1" stop-color="#123a6b"/>
      </linearGradient>
      <linearGradient id="strip" x1="0" y1="0" x2="0" y2="1">
        <stop offset="0" stop-color="#2c5f95"/>
        <stop offset="0.5" stop-color="#5d87b4"/>
        <stop offset="1" stop-color="#1c3f66"/>
      </linearGradient>
      <linearGradient id="bar" x1="0" y1="0" x2="0" y2="1">
        <stop offset="0" stop-color="#7cc3f0"/>
        <stop offset="1" stop-color="#5aaee6"/>
      </linearGradient>
      <linearGradient id="cta" x1="0" y1="0" x2="1" y2="0">
        <stop offset="0" stop-color="#e23a9c"/>
        <stop offset="1" stop-color="#f06cbd"/>
      </linearGradient>
    </defs>
    <rect class="band" x="0" y="154" width="680" height="418" fill="url(#band)"/>
    <rect class="band-strip" x="853" y="154" width="347" height="56" fill="url(#strip)"/>
    <rect class="copy-panel" x="853" y="208" width="347" height="308" fill="#050709"/>
    <polygon class="bar-fold" points="853,79 892,120 892,170 853,170" fill="#0d2f57"/>
    <rect class="title-bar" x="656" y="79" width="197" height="568" fill="url(#bar)"/>
    <polygon class="cta-shape" points="738,722 1200,722 1200,825 666,825" fill="url(#cta)"/>
  </svg>

  <div class="headline-small">HR</div>
  <div class="headline-big">HEADACHES</div>
  <p class="tagline">have you in the doghouse?</p>

  <div class="dog-photo" role="img" aria-label="Photo of a seated black and white border collie smiling at the viewer"></div>

  <div class="brand"><span class="brand-dot"></span>talentharbor</div>

  <div class="section-title"><span>WHAT DO WE DO?</span></div>

  <p class="service-copy">Hand off the headaches of payroll, hr &amp; compliance to talentharborsolutions and focus on the business of your business.</p>

  <div class="cta">CALL US NOW!</div>
</main>
</body>
</html>
```